lark to lead - dorian whitcombe personal speaking/consulting website

custom website for my personal speaking/consulting services brand, you can see the basic site we are using as a placeholder at www.larktolead.example now. I want to re-position this to more of a personal brand site and have video samples of speaking events, downloadable content, a video blog, and links to podcast. I really like the design of marcoveldin.example and the feature set should be fairly similar to his. I'll begin to compile more stock images etc. to use for sliders like he has done, for now we'll need to use stock imagery or existing photography from my social accounts. You can get a feel for social at all platforms/dwhitrealty i.e. facebook.com/dwhitrealty. the site should be primarily geared toward showcasing speaking/consulting services and content, as well as be flexible to allow for additional downloadables etc. in the future.

Target Market(s)

entrepreneurs and leaders looking to grow themselves, their business, and those they lead.

Coding

Coded - Design and coding required

Number of Pages Required

3 page

Font styles to use
Sans Serif

Colors

Designer to choose colors to be used in the design.

Requirements
Must have
• modern slick design, video blog, podcast feed, registration for people to subscribe to newsletter

```html
<!DOCTYPE html>
<html lang="en">
<head>
<meta charset="utf-8">
<title>Lark to Lead — Dorian Whitcombe</title>
<link href="https://fonts.googleapis.com/css2?family=Poppins:wght@400;500;600&display=swap" rel="stylesheet">
<style>
:root{
  --red:#bd0000;
  --red-dark:#9c0000;
  --ink:#2b2b2b;
  --text:#3a3a3a;
  --muted:#6b6b6b;
  --grey-band:#efefef;
  --footer:#232323;
  --white:#ffffff;
  --line:#d6d6d6;
}
*{box-sizing:border-box;margin:0;padding:0}
html,body{width:1200px;height:3080px;overflow:hidden}
body{font-family:'Poppins',sans-serif;color:var(--text);background:var(--white);position:relative}
.abs{position:absolute}
.btn{position:absolute;background:var(--red);color:var(--white);font-weight:600;display:flex;align-items:center;justify-content:center;border-radius:2px;font-size:15px}

/* top bar */
.topbar{left:0;top:0;width:1200px;height:54px;background:var(--red);color:var(--white);font-size:15px}
.topbar .contact{left:135px;top:0;height:54px;display:flex;align-items:center;gap:16px}
.topbar .contact span{display:flex;align-items:center;gap:7px}
.topbar nav{right:144px;top:0;height:54px;display:flex;align-items:center;gap:28px;font-size:15px}

/* hero */
.hero{left:0;top:54px;width:1200px;height:462px;background:linear-gradient(180deg,#3f4348 0%,#2a2d31 55%,#4a4e52 100%)}
.hero-portrait{left:135px;top:20px;width:440px;height:442px;background:radial-gradient(ellipse at 50% 40%,#5a4a40 0%,#2a2424 60%,rgba(30,30,30,0) 100%)}
.hero-arrow{top:218px;width:32px;height:28px;background:#444;border:1px solid #888;display:flex;align-items:center;justify-content:center}
.hero-brand{left:640px;top:215px;color:var(--white);font-size:44px;font-weight:600;letter-spacing:.5px}
.hero-brand::before{content:"";display:inline-block;width:14px;height:14px;border-radius:50%;background:var(--white);margin-right:12px;vertical-align:middle}
.hero-tagline{left:640px;top:312px;color:var(--white);font-size:26px;line-height:37px}

/* subscribe */
.subscribe{left:237px;top:466px;width:729px;height:189px;background:var(--white);border-top:4px solid var(--red);box-shadow:0 6px 18px rgba(0,0,0,.12)}
.subscribe p{position:absolute;left:50px;right:50px;top:36px;text-align:center;font-size:17px;line-height:25px;color:var(--ink)}
.subscribe .field{left:73px;top:101px;width:290px;height:38px;border:1px solid var(--line);font-size:11px;color:#555;padding:0 10px;display:flex;align-items:center}
.subscribe .btn{left:371px;top:101px;width:282px;height:37px;font-weight:500;font-size:19px}

/* training */
.section-title{width:1200px;left:0;text-align:center;font-size:38px;font-weight:500;color:var(--ink)}
.divider{left:567px;width:66px;height:1px;background:#444}
.intro{left:160px;width:880px;text-align:center;font-size:13px;line-height:24px;color:#222}
.feature{top:848px;width:260px;text-align:center}
.feature .ring{width:96px;height:96px;border-radius:50%;border:3px solid var(--red);margin:0 auto;display:flex;align-items:center;justify-content:center;background:var(--white);box-shadow:0 8px 6px -6px rgba(0,0,0,.25)}
.feature h3{margin-top:30px;font-size:18px;font-weight:500;color:#555}
.feature p{margin-top:12px;font-size:13px;line-height:23px;color:#222}

/* about */
.about-band{left:0;top:1206px;width:1200px;height:475px;background:var(--grey-band)}
.about-photo{left:133px;top:1292px;width:394px;height:302px;background:linear-gradient(90deg,#2c2624 0%,#4a3a34 40%,var(--red) 70%)}
.about-photo .brand{position:absolute;left:255px;top:90px;color:var(--white);font-size:22px;font-weight:600}
.about-photo .name{position:absolute;left:258px;top:133px;color:var(--white);font-size:15px}
.about h2{font-size:32px;font-weight:400;color:var(--ink)}
.about-copy{left:586px;top:1336px;width:470px;font-size:13px;line-height:23px;color:var(--muted)}
.about-copy p{margin-bottom:5px}
.ticks{list-style:none;margin-top:8px}
.ticks li{display:flex;align-items:center;gap:12px;margin-bottom:10px}

/* media */
.media{background:linear-gradient(135deg,#c8c2b6 0%,#8d8678 45%,#3b56a8 100%)}
.media.suit{background:linear-gradient(120deg,#e8e8e8 0%,#bbb 30%,#2d2d2d 55%,#6c7f5a 85%,#e6e6e6 100%)}
.media.chat{background:linear-gradient(90deg,#d9d9d9 0%,#c7c7c7 45%,#c0262a 70%,#caa088 100%)}
.media-label{position:absolute;top:106px;height:36px;padding:0 27px;background:rgba(200,60,60,.88);color:var(--white);font-weight:600;font-size:17px;display:flex;align-items:center}

.download h2{font-size:34px;font-weight:400;color:var(--ink)}
.download-copy{left:133px;top:2132px;width:460px;font-size:13px;line-height:23px;color:var(--muted)}
.download-copy span{color:#222}

/* inquiry */
.footer{left:0;top:2757px;width:1200px;height:278px;background:var(--footer);color:var(--white)}
.inquiry{left:232px;top:2406px;width:706px;height:373px;background:var(--white);box-shadow:0 4px 16px rgba(0,0,0,.15);border-radius:3px}
.inquiry::before,.inquiry::after{content:"";position:absolute;left:57px;width:594px;height:4px;background:repeating-linear-gradient(90deg,#e07070 0 14px,#bbb 14px 18px)}
.inquiry::before{top:0}
.inquiry::after{bottom:0}
.inquiry h2{position:absolute;left:0;top:22px;width:100%;text-align:center;font-size:32px;font-weight:400;color:var(--ink)}
.input{position:absolute;height:42px;border:1px solid var(--line);display:flex;align-items:center;font-size:11px;color:#555}
.input .ico{width:36px;height:26px;display:flex;align-items:center;justify-content:center;border-right:1px solid var(--line);margin-right:12px}
.input.msg{align-items:flex-start;padding-top:8px}
.inquiry .btn{left:323px;top:301px;width:90px;height:35px;font-size:19px;font-weight:500}

.footer h4{position:absolute;top:73px;font-size:17px;font-weight:500}
.links{left:133px;top:113px;list-style:none;font-size:13px;line-height:27px}
.links li::before{content:"›";margin-right:7px;font-size:15px}
.details{left:410px;top:108px;font-size:13px;line-height:19px}
.details div{display:flex;gap:14px;margin-bottom:18px}
.details svg{flex:none}
.footer-brand{left:830px;top:148px;font-size:38px;font-weight:600;display:flex;align-items:center;gap:12px}
.footer-brand i{width:18px;height:18px;border-radius:50%;background:var(--white);display:block}

.bottombar{left:0;top:3035px;width:1200px;height:45px;background:var(--red);color:var(--white);font-size:13px}
.bottombar p{position:absolute;left:135px;top:13px}
.social{position:absolute;top:9px;width:27px;height:27px;border:1px solid rgba(255,255,255,.8)}
</style>
</head>
<body>

<header class="abs topbar">
  <div class="abs contact">
    <span><svg width="20" height="20" viewBox="0 0 24 24" fill="none" stroke="#fff" stroke-width="1.6"><path d="M5 3h4l2 5-2.5 1.5a11 11 0 0 0 6 6L16 13l5 2v4a2 2 0 0 1-2 2A17 17 0 0 1 3 5a2 2 0 0 1 2-2z"/></svg>555 014 2287 2287</span>
    <span><svg width="20" height="20" viewBox="0 0 24 24" fill="none" stroke="#fff" stroke-width="1.6"><rect x="3" y="6" width="18" height="13"/><path d="M3 6l9 7 9-7"/></svg>dorian@dwhitrealty.example</span>
  </div>
  <nav class="abs"><span>Home</span><span>Resources</span><span>Contact Us</span></nav>
</header>

<section class="abs hero">
  <div class="abs hero-portrait" role="img" aria-label="Portrait of Dorian Whitcombe in a dark suit and red tie over a city skyline"></div>
  <div class="abs hero-arrow" style="left:2px"><svg width="10" height="12" viewBox="0 0 10 12"><path d="M7 1L2 6l5 5" stroke="#fff" stroke-width="2" fill="none"/></svg></div>
  <div class="abs hero-arrow" style="left:1163px"><svg width="10" height="12" viewBox="0 0 10 12"><path d="M3 1l5 5-5 5" stroke="#fff" stroke-width="2" fill="none"/></svg></div>
  <div class="abs hero-brand">Lark to Lead</div>
  <div class="abs hero-tagline">The Place Where Entrepreneurs<br>Come To Become Leaders</div>
</section>

<form class="abs subscribe">
  <p>Subscribe To This Blog To Get The Latest Tips And Tricks To Help You Be A Successful Enterpreneur</p>
  <div class="abs field">Email address</div>
  <div class="btn">Subscribe to our Podcast</div>
</form>

<h2 class="abs section-title" style="top:714px">Start Your Training Today</h2>
<div class="abs divider" style="top:777px"></div>
<p class="abs intro" style="top:786px">Lorem ipsum dolor sit amet, consectetuer adipiscing elit, sed diam nonummy nibh euismod tincidunt ut laoreet dolore magna aliquam erat volutpat. Ut wisi enim ad minim veniam.</p>

<div class="abs feature" style="left:146px">
  <div class="ring"><svg width="56" height="44" viewBox="0 0 56 44" fill="#222"><circle cx="28" cy="9" r="5"/><rect x="23" y="16" width="10" height="16" rx="3"/><circle cx="12" cy="14" r="4"/><rect x="8" y="20" width="8" height="14" rx="2"/><circle cx="44" cy="14" r="4"/><rect x="40" y="20" width="8" height="14" rx="2"/><circle cx="3" cy="17" r="3"/><rect x="0" y="22" width="6" height="12" rx="2"/><circle cx="53" cy="17" r="3"/><rect x="50" y="22" width="6" height="12" rx="2"/></svg></div>
  <h3>Leadership Skills</h3>
  <p>Lorem ipsum dolor sit amet, consuer adipiscing elit, sed diam nonummy nibh euismod tincidunt ut.</p>
</div>
<div class="abs feature" style="left:465px">
  <div class="ring"><svg width="46" height="46" viewBox="0 0 46 46" fill="none" stroke="#222" stroke-width="3"><circle cx="23" cy="22" r="9"/><path d="M19 34h8M20 38h6M23 3v5M8 9l4 4M38 9l-4 4M3 22h5M38 22h5"/></svg></div>
  <h3>Entrepreneurs</h3>
  <p>Lorem ipsum dolor sit amet, consuer adipiscing elit, sed diam nonummy nibh euismod tincidunt ut.</p>
</div>
<div class="abs feature" style="left:783px">
  <div class="ring"><svg width="50" height="48" viewBox="0 0 50 48" fill="#222"><circle cx="25" cy="6" r="5"/><rect x="21" y="12" width="8" height="12" rx="2"/><circle cx="12" cy="20" r="4"/><rect x="8" y="26" width="8" height="20" rx="2"/><circle cx="38" cy="20" r="4"/><rect x="34" y="26" width="8" height="20" rx="2"/><rect x="16" y="26" width="18" height="5"/></svg></div>
  <h3>Team Building</h3>
  <p>Lorem ipsum dolor sit amet, consuer adipiscing elit, sed diam nonummy nibh euismod tincidunt ut.</p>
</div>
<div class="btn" style="left:526px;top:1101px;width:147px;height:35px;font-size:16px">Get Started</div>

<section class="abs about-band"></section>
<div class="abs about-photo" role="img" aria-label="Dorian Whitcombe smiling in a suit on a red background">
  <div class="brand">Lark to Lead</div>
  <div class="name">Dorian Whitcombe</div>
</div>
<div class="abs about" style="left:586px;top:1276px"><h2>About Me</h2></div>
<div class="abs about-copy">
  <p>Dlore magna aliquam erat volutpat. Ut wisi enim ad minim veniam, quis nostrud exerci.</p>
  <p>Lorem ipsum dolor sit amet, consectetuer adipiscing elit, sed donummy nibh euismod tincidunt ut laoreet dolore magna aliquam erat volutpat. Ut wisi enim ad minim veniam, quis nostrud exerci.</p>
  <ul class="ticks">
    <li><svg width="15" height="15" viewBox="0 0 16 16" fill="none" stroke="#bd0000" stroke-width="1.6"><circle cx="8" cy="8" r="6.5"/><path d="M5 8l2.5 2.5L15 3"/></svg>Duis autem vel eum iriure dolor in hendrerit in vulputate.</li>
    <li><svg width="15" height="15" viewBox="0 0 16 16" fill="none" stroke="#bd0000" stroke-width="1.6"><circle cx="8" cy="8" r="6.5"/><path d="M5 8l2.5 2.5L15 3"/></svg>Velit esse olestie consequat, vel illum dolore eu feugiat.</li>
    <li><svg width="15" height="15" viewBox="0 0 16 16" fill="none" stroke="#bd0000" stroke-width="1.6"><circle cx="8" cy="8" r="6.5"/><path d="M5 8l2.5 2.5L15 3"/></svg>Nulla facilisis at vero erocumsan et iusto odio dignissim qui.</li>
  </ul>
</div>
<div class="btn" style="left:587px;top:1563px;width:148px;height:35px">Contact Us Today</div>

<div class="abs media" style="left:133px;top:1752px;width:437px;height:247px" role="img" aria-label="Video still of Dorian Whitcombe speaking in a blue polo shirt">
  <div class="media-label" style="left:122px">Podcasts</div>
</div>
<div class="abs media suit" style="left:613px;top:1752px;width:436px;height:247px" role="img" aria-label="Video still of Dorian Whitcombe in a suit at a speaking event">
  <div class="media-label" style="left:134px;padding:0 10px">Speaking Events</div>
</div>

<div class="abs download" style="left:133px;top:2080px"><h2>Downloadable Content</h2></div>
<div class="abs download-copy">
  <p>Dlore magna aliquam erat volutpat. Ut wisi enim ad minim veniam, quis nostrud exerci.</p>
  <p style="margin-top:6px">Ready for more? <span>Lorem ipsum dolor sit amet, consectetuer adipiscing elit, sed diam nonummy nibh euismod tincidunt ut laoreet dolore magna aliquam erat volutpat.</span></p>
</div>
<div class="btn" style="left:133px;top:2261px;width:204px;height:35px">Visit Our Resources Page</div>
<div class="abs media chat" style="left:613px;top:2071px;width:436px;height:247px" role="img" aria-label="Video blog still of Dorian Whitcombe in a red shirt in front of a whiteboard"></div>

<footer class="abs footer">
  <h4 style="left:133px">Quick Links</h4>
  <ul class="abs links"><li>Home</li><li>About Me</li><li>Services</li><li>Resources</li><li>Contact Us</li></ul>
  <h4 style="left:416px">Contact Details</h4>
  <div class="abs details">
    <div><svg width="14" height="18" viewBox="0 0 14 18"><path d="M7 0a7 7 0 0 0-7 7c0 5 7 11 7 11s7-6 7-11a7 7 0 0 0-7-7z" fill="#bd0000"/><circle cx="7" cy="7" r="2.5" fill="#232323"/></svg><span style="padding-left:8px">Street Name, City Name, State<br>Zipcode</span></div>
    <div><svg width="18" height="18" viewBox="0 0 24 24" fill="none" stroke="#bd0000" stroke-width="1.6"><rect x="3" y="6" width="18" height="13"/><path d="M3 6l9 7 9-7"/></svg><span style="padding-left:4px">dorian@dwhitrealty.example</span></div>
    <div><svg width="18" height="18" viewBox="0 0 24 24" fill="none" stroke="#bd0000" stroke-width="1.6"><path d="M5 3h4l2 5-2.5 1.5a11 11 0 0 0 6 6L16 13l5 2v4a2 2 0 0 1-2 2A17 17 0 0 1 3 5a2 2 0 0 1 2-2z"/></svg><span style="padding-left:4px">555 014 2287 2287</span></div>
  </div>
  <div class="abs footer-brand"><i></i>Lark to Lead</div>
</footer>

<form class="abs inquiry">
  <h2>Quick Inquiry</h2>
  <div class="input" style="left:56px;top:89px;width:289px"><span class="ico"><svg width="11" height="12" viewBox="0 0 11 12" fill="#bd0000"><circle cx="5.5" cy="3" r="3"/><path d="M0 12a5.5 5 0 0 1 11 0z"/></svg></span>First Name*</div>
  <div class="input" style="left:361px;top:89px;width:289px"><span class="ico"><svg width="11" height="12" viewBox="0 0 11 12" fill="#bd0000"><circle cx="5.5" cy="3" r="3"/><path d="M0 12a5.5 5 0 0 1 11 0z"/></svg></span>Last Name*</div>
  <div class="input" style="left:56px;top:144px;width:289px"><span class="ico"><svg width="12" height="12" viewBox="0 0 24 24" fill="#bd0000"><path d="M5 2h4l2 5-3 2a12 12 0 0 0 7 7l2-3 5 2v4a3 3 0 0 1-3 3A19 19 0 0 1 2 5a3 3 0 0 1 3-3z"/></svg></span>Your Phone*</div>
  <div class="input" style="left:361px;top:144px;width:289px"><span class="ico"><svg width="13" height="10" viewBox="0 0 13 10" fill="#bd0000"><rect width="13" height="10"/><path d="M0 0l6.5 5L13 0" stroke="#fff" fill="none"/></svg></span>Your Email*</div>
  <div class="input msg" style="left:56px;top:199px;width:594px;height:84px"><span class="ico"><svg width="14" height="11" viewBox="0 0 14 11" fill="#bd0000"><ellipse cx="5.5" cy="4" rx="5.5" ry="4"/><ellipse cx="9" cy="6.5" rx="5" ry="3.5"/></svg></span>Your Message*</div>
  <div class="btn">Submit</div>
</form>

<div class="abs bottombar">
  <p>Copyright © 2019 Bright Harbor. All Right Reserved</p>
  <span class="social" style="left:952px" aria-label="Social profile"></span>
  <span class="social" style="left:988px" aria-label="Social profile"></span>
  <span class="social" style="left:1023px" aria-label="Social profile"></span>
</div>

</body>
</html>
```